Website Design

This is a Website design project for a Software Developer / Consulting Company called Quindlex.

I would like to have a place for : blogs, partners, products, solutions and whatever you recommend. It would be nice to have a slot for Case Studies and Video Training.

I like our Competitor's site www.vorantix.example
I DO NOT LIKE our competitor's MAIN Page: www.sulvendo.example.
Although Sulvendo does have a nice way of putting blog news and twitter. below their webpage.

There should be a place for us to change our Logo: i.e. Like MIRALOO. EVeryday miraloo changes its logo color.

thanks

Kelmor
Updates

Deisgns look good. However, I would like to see more deisgn options. Please be a little creative. thank you

Kelmor

Reason: We need to do some more modifications. We will be narrowing down the selections and working with Designers to get it to final stage.

Industry/Entity Type

It Company

```html
<!DOCTYPE html>
<html lang="en">
<head>
<meta charset="utf-8">
<title>Quindlex</title>
<link rel="stylesheet" href="https://fonts.googleapis.com/css2?family=Bebas+Neue&family=Open+Sans:ital,wght@0,400;0,600;0,700;1,400&family=Oswald:wght@400;500&family=Raleway:wght@400&display=swap">
<style>
:root{
  --green:#6ab42f;
  --blue:#2e62b0;
  --slate:#3b4456;
  --ink:#222;
  --line:#e4e4e4;
  --footer:#1d1d1d;
  --white:#fff;
}
*{margin:0;padding:0;box-sizing:border-box}
html,body{width:800px;height:1200px;overflow:hidden}
body{position:relative;background:var(--white);font-family:"Open Sans",Arial,sans-serif;color:var(--ink)}
.abs{position:absolute}
.display{font-family:"Bebas Neue",Impact,sans-serif;font-weight:400;letter-spacing:.5px}

/* promo banner */
.promo{left:99px;top:0;width:603px;height:237px;background:linear-gradient(90deg,#78bd3f 0%,#8cc857 55%,#7bbd44 100%)}
.promo-title{left:34px;top:36px;width:320px;font-size:38px;line-height:38px;color:var(--white)}
.promo-text{left:34px;top:120px;font-family:"Raleway",Arial,sans-serif;font-size:9.5px;line-height:13px;color:#eaf5dd;text-transform:uppercase;white-space:nowrap}
.promo-btn{left:34px;top:156px;width:147px;height:32px;border:1.5px solid var(--white);color:var(--white);font-family:"Raleway",Arial,sans-serif;font-size:15px;display:flex;align-items:center;justify-content:center}
.promo-device{left:397px;top:20px;width:118px;height:200px;border-radius:10px;background:linear-gradient(160deg,#3a3a3a,#111 60%,#2a2a2a)}
.dots{display:flex;gap:5px}
.dot{width:9px;height:9px;border-radius:50%;background:var(--ink)}
.dot.on{background:var(--white)}
.promo .dots{left:262px;top:216px}

.stripe{left:0;top:245px;width:800px;height:8px;background:var(--green)}

/* header */
.logo{left:99px;top:265px;display:flex;align-items:center;gap:8px}
.logo-word{font-size:25px;font-weight:600;color:var(--green);letter-spacing:-.5px}
.nav{left:465px;top:253px;height:62px;display:flex;align-items:center;font-family:"Oswald",sans-serif;font-size:10.5px;color:#444;letter-spacing:.3px}
.nav span{margin-right:12px}
.nav-active{left:636px;top:253px;width:64px;height:62px;background:var(--green);color:var(--white);font-family:"Oswald",sans-serif;font-size:10.5px;display:flex;align-items:center;justify-content:center;font-weight:500}
.dropdown{left:636px;top:316px;width:107px;z-index:5;background:#eee;border-bottom:3px solid var(--green);box-shadow:0 2px 4px rgba(0,0,0,.2);font-size:8.5px;color:#777}
.dropdown div{height:18px;line-height:18px;padding-left:10px;border-bottom:1px solid #ddd}
.dropdown .current{background:var(--green);color:var(--white)}

/* hero */
.hero{left:0;top:315px;width:800px;height:302px;background:linear-gradient(120deg,#7e95ab 0%,#c9b8a8 35%,#a2806a 55%,#d7c8bb 75%,#6f8aa5 100%)}
.arrow{top:131px}
.caption{left:101px;top:185px;width:412px;height:107px;background:rgba(40,40,40,.45)}
.caption-title{left:12px;top:8px;font-size:44px;line-height:44px;color:var(--white)}
.caption-text{left:12px;top:50px;font-size:18.5px;line-height:21px;color:var(--white)}
.bars{left:603px;top:289px;display:flex;gap:4px}
.bars span{width:29px;height:4px;background:var(--white)}
.bars .on{background:var(--green)}

/* service cards */
.card{top:636px;width:192px;height:187px;color:var(--white)}
.card.blue{left:99px;background:var(--blue)}
.card.green{left:304px;background:var(--green)}
.card.slate{left:508px;background:var(--slate)}
.card-label{left:10px;right:10px;top:12px;padding-bottom:6px;border-bottom:1px solid rgba(255,255,255,.6);text-align:center;font-size:10px;font-weight:600;text-transform:uppercase}
.card-title{left:10px;top:38px;font-size:27px;line-height:25px;width:170px}
.card-text{left:10px;top:94px;font-size:7px;line-height:12px;font-weight:600;text-transform:uppercase;white-space:nowrap}
.card-btn{left:10px;top:148px;width:75px;height:24px;border:1px solid var(--white);font-size:7.5px;font-weight:700;display:flex;align-items:center;justify-content:center;gap:8px}

.divider{left:40px;width:720px;height:8px;background:radial-gradient(ellipse at top,rgba(0,0,0,.12),transparent 70%)}

/* testimonials */
.section-title{left:0;width:800px;text-align:center;font-size:26px;color:var(--ink)}
.avatar{left:127px;top:897px;width:88px;height:88px;border-radius:50%;border:3px solid var(--white);box-shadow:0 0 0 2px #ccc,0 2px 5px rgba(0,0,0,.3);background:radial-gradient(circle at 50% 40%,#c99a7b,#8a5d43 70%,#5a4a40)}
.quote-box{left:236px;top:903px;width:440px;height:97px;border:1px solid var(--line);box-shadow:0 1px 3px rgba(0,0,0,.08)}
.quote-mark{font-family:Georgia,serif;font-size:30px;font-weight:700;color:var(--ink);line-height:30px}
.quote-close{font-family:Georgia,serif;font-size:24px;font-weight:700;font-style:normal;color:var(--ink);line-height:10px;vertical-align:-10px;margin-left:4px}
.quote-text{left:35px;top:12px;width:395px;font-size:10px;line-height:15px;font-style:italic;color:#444}
.quote-author{left:40px;top:76px;font-size:10px;font-style:italic;color:var(--green)}
.t-dots{left:351px;top:1011px}
.t-dots .on{background:var(--green)}

/* clients */
.clients{left:115px;top:1092px;width:570px;display:flex;justify-content:space-between;align-items:center;font-size:16px;font-weight:600;color:#9a9a9a}

/* footer */
.footer{left:0;top:1147px;width:800px;height:53px;background:var(--footer);border-top:3px solid var(--green)}
.footer-nav{left:101px;top:10px;display:flex;gap:16px;font-family:"Oswald",sans-serif;font-size:10px;color:#ddd}
.copyright{left:101px;top:29px;font-size:9.5px;color:#bbb}
.social{left:618px;top:10px;display:flex;gap:4px}
.social span{width:18px;height:18px;background:#555;border-radius:2px}
</style>
</head>
<body>

<section class="promo abs">
  <h1 class="promo-title abs display">Lorem Ipsum is simply dummy</h1>
  <p class="promo-text abs">Lorem Ipsum is simply dummy text of the printing<br>and typesetting industry. Lorem Ipsum</p>
  <div class="promo-btn abs">Watch Video</div>
  <div class="promo-device abs" role="img" aria-label="Smartphone showing app icons on its screen"></div>
  <div class="dots abs"><span class="dot on"></span><span class="dot"></span><span class="dot"></span></div>
</section>

<div class="stripe abs"></div>

<section class="hero abs" role="img" aria-label="Cupped hands holding soil with a young green seedling">
  <svg class="arrow abs" style="left:40px" width="22" height="38" viewBox="0 0 22 38"><path d="M19 3 L4 19 L19 35" fill="none" stroke="#fff" stroke-width="4"/></svg>
  <svg class="arrow abs" style="left:738px" width="22" height="38" viewBox="0 0 22 38"><path d="M3 3 L18 19 L3 35" fill="none" stroke="#fff" stroke-width="4"/></svg>
  <div class="caption abs">
    <h2 class="caption-title abs display">Web Solutions</h2>
    <p class="caption-text abs">Get noticed, go functional Trendy<br>we designs that connect</p>
  </div>
  <div class="bars abs"><span class="on"></span><span></span><span></span></div>
</section>

<header>
  <div class="logo abs">
    <svg width="36" height="36" viewBox="0 0 36 36"><circle cx="18" cy="18" r="16" fill="var(--ink)"/></svg>
    <span class="logo-word">Quindlex</span>
  </div>
  <nav class="nav abs"><span>PUBLISHER</span><span>BUYERNETWORK</span><span>MOBILE</span></nav>
  <div class="nav-active abs">PLATFORM</div>
  <div class="dropdown abs">
    <div>PUBLISHER BUYER</div>
    <div class="current">NETWORK</div>
    <div>MOBILE ETC</div>
  </div>
</header>

<section class="services">
  <article class="card blue abs">
    <h3 class="card-label abs">Application Development</h3>
    <p class="card-title abs display">Lorem Ipsum is simply dummy</p>
    <p class="card-text abs">Lorem Ipsum is simply dummy text of<br>the printing and typesetting industry.<br>Lorem Ipsum</p>
    <div class="card-btn abs">READ MORE <span>›</span></div>
  </article>
  <article class="card green abs">
    <h3 class="card-label abs">Web&nbsp; Development</h3>
    <p class="card-title abs display">Lorem Ipsum is simply dummy</p>
    <p class="card-text abs">Lorem Ipsum is simply dummy text of<br>the printing and typesetting industry.<br>Lorem Ipsum</p>
    <div class="card-btn abs">READ MORE <span>›</span></div>
  </article>
  <article class="card slate abs">
    <h3 class="card-label abs">Web &amp; User Interface Design</h3>
    <p class="card-title abs display">Lorem Ipsum is simply dummy</p>
    <p class="card-text abs">Lorem Ipsum is simply dummy text of<br>the printing and typesetting industry.<br>Lorem Ipsum</p>
    <div class="card-btn abs">READ MORE <span>›</span></div>
  </article>
</section>

<div class="divider abs" style="top:843px"></div>

<section class="testimonials">
  <h2 class="section-title abs display" style="top:862px">Testimonials</h2>
  <div class="avatar abs" role="img" aria-label="Portrait photo of a smiling client"></div>
  <div class="quote-box abs">
    <span class="quote-mark abs" style="left:10px;top:6px">“</span>
    <p class="quote-text abs">Lorem Ipsum is simply dummy text of the printing and typesetting industry. Lorem Ipsum has been the industry's standard dummy text ever since the 1500s, when an unknown printer took a galley of type and scrambled it to make a type specimen book. It has survived not only five centuries,<span class="quote-close">”</span></p>
    <p class="quote-author abs">- Lorem Ipsum is simply</p>
  </div>
  <div class="dots t-dots abs"><span class="dot on"></span><span class="dot"></span><span class="dot"></span><span class="dot"></span></div>
</section>

<div class="divider abs" style="top:1032px"></div>

<section class="our-clients">
  <h2 class="section-title abs display" style="top:1047px">Our Clients</h2>
  <div class="clients abs">
    <span>Quorvane</span><span>Zelphi</span><span>Marnoxa</span><span>Fenwilt</span><span>Drubix</span><span>Tolvern</span><span>Yskai</span><span>Plontra</span><span>Wembrix</span>
  </div>
</section>

<footer class="footer abs">
  <nav class="footer-nav abs"><span>HOME</span><span>PRODUCTS</span><span>SOLUTIONS</span><span>LEARN</span><span>SUPPORT</span><span>PARTNERS</span><span>COMPANY</span></nav>
  <p class="copyright abs">© 2014 Quindlex Inc. All rights reserved</p>
  <div class="social abs"><span></span><span></span><span></span><span></span></div>
</footer>

</body>
</html>
```